EdTech Pellino

We am looking for complete redesign of our Mobile learning app and looking for a simple and best UI/UX design and ICON for our App. I have mentioned our app link below .
We sell Mobile app for students who prepares for Medical exams Educational apps.

We like a simple design , you can refer these apps
https://apps.storefrontdemo.test/us/app/vorlix-learn-languages-spanish-french-more/id504918273?mt=8

https://market.droidshelf.test/store/apps/details?id=fi.kx.android.tarvella&hl=en

our app:
IOS APP
https://apps.storefrontdemo.test/us/app/qorm-brevatel-rn-exam-prep-2017-edition/id1739025418?mt=8
Android
https://market.droidshelf.test/store/apps/details?id=com.pellinoworks.elearning.android.brevatelrn&hl=en

Target Market(s)

Our target audience are Medical student , age of 20 to 40

Industry/Entity Type

Medical

Font styles to use
Sans Serif

Colors
33a6d7
72c9bd
faa54b
f68d4d
3176b5

Requirements
Must have
• Icon and UX
Nice to have
• a better design for our test history as well

```html
<!DOCTYPE html>
<html lang="en">
<head>
<meta charset="utf-8">
<title>Respiratory Quiz Screen</title>
<link href="https://fonts.googleapis.com/css2?family=Raleway:wght@400;500&display=swap" rel="stylesheet">
<style>
  :root {
    --bg: #ffffff;
    --ink: #2f3d44;
    --ink-soft: #5e7178;
    --panel: #f3f7f8;
    --divider: #dfe8ea;
    --radio: #cfe3e6;
    --teal: #66c2b3;
    --icon: #ffffff;
    --figure-a: #eef3f4;
    --figure-b: #f8fafb;
  }
  * { box-sizing: border-box; margin: 0; padding: 0; }
  html, body { width: 740px; height: 1200px; overflow: hidden; background: var(--bg); }
  body { font-family: "Raleway", sans-serif; color: var(--ink); position: relative; }

  .top-bar { position: absolute; top: 0; left: 0; width: 740px; height: 104px; }
  .top-bar .back { position: absolute; left: 44px; top: 36px; }
  .top-bar .menu { position: absolute; right: 46px; top: 38px; }
  .top-bar .title {
    position: absolute; top: 36px; width: 100%; text-align: center;
    font-size: 25px; font-weight: 400; color: var(--ink-soft); letter-spacing: .2px;
  }

  .figure {
    position: absolute; left: 134px; top: 118px; width: 472px; height: 414px;
    background: linear-gradient(180deg, var(--figure-b), var(--figure-a));
    border-radius: 12px;
  }

  .question {
    position: absolute; top: 588px; left: 60px; width: 620px; text-align: center;
    font-size: 25px; line-height: 32px; font-weight: 400; color: var(--ink);
  }

  .options {
    position: absolute; top: 744px; left: 0; width: 740px; height: 360px;
    background: var(--panel); list-style: none; padding-top: 26px;
  }
  .option {
    display: flex; align-items: center; margin: 0 56px 0 76px; height: 72px;
    border-bottom: 2px solid var(--divider); font-size: 24px; font-weight: 500;
  }
  .option:last-child { border-bottom: none; }
  .option .radio {
    width: 38px; height: 38px; border-radius: 50%; background: var(--radio);
    margin-left: 0; margin-right: 44px;
  }

  .tab-bar {
    position: absolute; bottom: 0; left: 0; width: 740px; height: 96px;
    background: var(--teal);
  }
  .tab-bar svg { position: absolute; top: 24px; }
</style>
</head>
<body>
  <header class="top-bar">
    <svg class="back" width="20" height="34" viewBox="0 0 20 34"><path d="M17 2 L3 17 L17 32" fill="none" stroke="var(--ink-soft)" stroke-width="2.4"/></svg>
    <h1 class="title">Respiratory 1 of 25</h1>
    <svg class="menu" width="40" height="26" viewBox="0 0 40 26"><path d="M0 2H40M0 13H40M0 24H40" stroke="var(--ink-soft)" stroke-width="2"/></svg>
  </header>

  <div class="figure" role="img" aria-label="Line drawing of a male torso with four labelled sites A to D: A at the right upper arm, B at the left upper arm, C over the left chest, D at the right shoulder"></div>

  <p class="question">A nurse must obtain a clients apical pulse.<br>Select the site where the nurse should<br>place the stethoscope.</p>

  <ul class="options">
    <li class="option"><span class="radio"></span>A</li>
    <li class="option"><span class="radio"></span>B</li>
    <li class="option"><span class="radio"></span>C</li>
    <li class="option"><span class="radio"></span>D</li>
  </ul>

  <nav class="tab-bar">
    <svg style="left:86px" width="48" height="48" viewBox="0 0 48 48" fill="none" stroke="var(--icon)" stroke-width="2.4" stroke-linejoin="round">
      <path d="M4 10 H20 Q24 10 24 14 V42 Q24 38 20 38 H4 Z"/>
      <path d="M44 10 H28 Q24 10 24 14 V42 Q24 38 28 38 H44 Z"/>
      <path d="M2 14 V42 H46 V14"/>
    </svg>
    <svg style="left:254px" width="40" height="48" viewBox="0 0 40 48" fill="none" stroke="var(--icon)" stroke-width="2.4" stroke-linejoin="round">
      <path d="M4 3 H26 L36 13 V45 H4 Z"/>
      <path d="M26 3 V13 H36"/>
      <path d="M11 36 L17 20 L23 36 M13 31 H21"/>
      <path d="M25 22 H31 M28 19 V25"/>
    </svg>
    <svg style="left:442px" width="34" height="48" viewBox="0 0 34 48" fill="none" stroke="var(--icon)" stroke-width="2.6" stroke-linejoin="round">
      <path d="M3 3 H31 V45 L17 31 L3 45 Z"/>
    </svg>
    <svg style="left:604px" width="50" height="50" viewBox="0 0 50 50" fill="none" stroke="var(--icon)" stroke-width="2.4" stroke-linecap="round" stroke-linejoin="round">
      <path d="M9 32 A19 19 0 1 0 10 13"/>
      <path d="M3 26 L9 33 L16 28"/>
      <path d="M18 25 L24 31 L35 18"/>
    </svg>
  </nav>
</body>
</html>
```